8x8 Social Media Ad - Harbor Summit Expo

Attention Real Estate Agents
Please join us for our
Quarterly Real Estate Training Expo
The 2nd Saturday of February, May, August and November
Our Next Training Expo is _________________________________
From 9 am to 1 pm
at
Marlowe Suites Fernridge Station
4187 Copperleaf Lane, Greenbelt, MD 20770
Scheduled Speakers
9:00 am - Desmond Pryce - Orientation
9:30 am - Terrell Oakes - Multiple Income Streams / Keystone Track
10:00 am - Lorna Beckett - Marketing though Social Media
10:45 am - Raul Denning - Generating Business through Kelp-Nest
11:30 am - Tunde Adesemi - Real Estate Investing
12:15 pm - Marcus Oyelowo - (Main Speaker) Training Topic TBA
For more information call Desmond Pryce at (240) 555-0192 or email dpryce@harborsummithomes.example

```html
<!DOCTYPE html>
<html lang="en">
<head>
<meta charset="utf-8">
<title>Harbor Summit Expo – Quarterly Real Estate Training Expo</title>
<link rel="stylesheet" href="https://fonts.googleapis.com/css2?family=Montserrat:ital,wght@0,400;0,600;0,700;0,800;1,300;1,400;1,700;1,800&display=swap">
<style>
:root{
  --teal-deep:#08514f;
  --teal-main:#0b6663;
  --teal-panel:#0a5c5a;
  --teal-light:#13918c;
  --teal-band:#1a8c88;
  --cyan:#2fe3d6;
  --yellow:#f8ea1c;
  --white:#ffffff;
  --ink:#0a4f4d;
}
*{box-sizing:border-box;margin:0;padding:0}
html,body{width:1200px;height:1200px;overflow:hidden}
body{font-family:"Montserrat",sans-serif;color:var(--white);background:var(--teal-main)}
.ad{position:relative;width:1200px;height:1200px;overflow:hidden;
  background:linear-gradient(160deg,var(--teal-light) 0%,var(--teal-main) 35%,var(--teal-deep) 100%)}
.ad__lower-glow{position:absolute;left:420px;top:642px;width:780px;height:558px;
  background:linear-gradient(180deg,#17a39d 0%,#0f7f7b 55%,#0a6461 100%)}

/* brand corner */
.brand{position:absolute;left:0;top:0;width:354px;height:138px;background:var(--white);
  border-bottom-right-radius:54px;display:flex;align-items:center;padding-left:46px;z-index:3}
.brand__name{font-weight:800;font-size:34px;color:var(--ink);letter-spacing:.5px}

/* speaker panel */
.speakers{position:absolute;left:36px;top:48px;width:450px;height:1046px;
  background:var(--teal-panel);border-radius:48px;z-index:1}
.speakers__tag{position:absolute;left:48px;top:168px;width:402px;height:54px;
  background:var(--teal-band);clip-path:polygon(0 0,100% 0,97% 100%,0 100%);
  display:flex;align-items:center;padding-left:26px;font-size:23px;font-weight:400;z-index:2;letter-spacing:.3px}
.speakers__tag strong{color:var(--cyan);font-weight:700;margin-left:8px}

.slot{position:absolute;left:42px;width:440px;height:132px;display:flex;align-items:center;z-index:2}
.slot__photo{width:132px;height:132px;border-radius:50%;flex:none;border:6px solid var(--cyan);
  background:radial-gradient(circle at 50% 40%,#5b4a40 0%,#2c2622 55%,var(--cyan) 56%,#26c9bf 100%)}
.slot__info{margin-left:22px;line-height:1.15}
.slot__time{font-style:italic;font-weight:400;font-size:29px}
.slot__name{color:var(--cyan);font-weight:800;font-size:23px;margin-top:6px;text-transform:uppercase}
.slot__topic{font-weight:700;font-size:15.5px;text-transform:uppercase;margin-top:3px;line-height:1.25}

/* headline */
.headline{position:absolute;left:520px;width:650px;text-align:center;text-transform:uppercase;line-height:1}
.headline--attention{top:102px}
.headline__thin{font-weight:300;font-style:italic;font-size:64px;display:block}
.headline__bold{font-weight:800;font-style:italic;font-size:66px;display:block;margin-top:4px}

.invite{position:absolute;left:516px;top:258px;width:654px;height:80px;background:var(--yellow);
  clip-path:polygon(4% 0,100% 0,96% 100%,0 100%);display:flex;align-items:center;justify-content:center;
  color:var(--ink);font-size:36px;text-transform:uppercase;font-weight:400}
.invite strong{font-weight:800;font-style:italic;margin-left:10px}

.headline--expo{top:360px}
.headline--expo .line{display:block;font-size:74px;font-style:italic;line-height:1.0}
.line--thin{font-weight:300}
.line--mixed b{font-weight:800}
.line--yellow{color:var(--yellow);font-weight:800}

/* schedule info */
.schedule{position:absolute;left:520px;top:712px;width:650px;text-align:center;text-transform:uppercase;
  font-size:40px;line-height:1.18;z-index:2}
.schedule__days{font-weight:800}
.schedule__next{font-weight:400;margin-top:4px}
.schedule__time{font-weight:800;color:var(--yellow)}

.venue{position:absolute;left:560px;top:976px;width:610px;display:flex;align-items:flex-start;z-index:2}
.venue__pin{width:40px;height:56px;flex:none;margin-top:12px}
.venue__text{margin-left:22px;font-size:29px;line-height:1.2;text-transform:uppercase;font-weight:400}

/* footer */
.contact{position:absolute;left:0;top:1130px;width:1200px;height:60px;z-index:2}
.contact__lead{position:absolute;left:26px;top:6px;font-size:19px;line-height:1.05;text-transform:uppercase;text-align:center}
.contact__phone{position:absolute;left:306px;top:6px;display:flex;align-items:center;font-weight:800;font-size:35px}
.contact__phone svg{width:34px;height:34px;margin-right:6px}
.contact__email{position:absolute;right:22px;top:0;font-size:24px;line-height:1.1;text-transform:uppercase;text-align:center}
</style>
</head>
<body>
<main class="ad">
  <div class="ad__lower-glow"></div>

  <div class="brand"><span class="brand__name">Harbor Summit</span></div>

  <section class="speakers" aria-label="Scheduled speakers"></section>
  <div class="speakers__tag">SCHEDULED<strong>SPEAKERS</strong></div>

  <div class="slot" style="top:234px">
    <div class="slot__photo" role="img" aria-label="Portrait of speaker Desmond Pryce"></div>
    <div class="slot__info"><div class="slot__time">9:00 AM</div><div class="slot__name">Desmond Pryce</div><div class="slot__topic">Orientation</div></div>
  </div>
  <div class="slot" style="top:378px">
    <div class="slot__photo" role="img" aria-label="Portrait of speaker Terrell Oakes"></div>
    <div class="slot__info"><div class="slot__time">9:30 AM</div><div class="slot__name">Terrell Oakes</div><div class="slot__topic">Multiple Income<br>Streams / Keystone Track</div></div>
  </div>
  <div class="slot" style="top:520px">
    <div class="slot__photo" role="img" aria-label="Portrait of speaker Lorna Beckett"></div>
    <div class="slot__info"><div class="slot__time">10:00 AM</div><div class="slot__name">Lorna Beckett</div><div class="slot__topic">Marketing<br>though Social Media</div></div>
  </div>
  <div class="slot" style="top:660px">
    <div class="slot__photo" role="img" aria-label="Portrait of speaker Raul Denning"></div>
    <div class="slot__info"><div class="slot__time">10:45 AM</div><div class="slot__name">Raul Denning</div><div class="slot__topic">Generating Business<br>through Kelp-Nest</div></div>
  </div>
  <div class="slot" style="top:804px">
    <div class="slot__photo" role="img" aria-label="Portrait of speaker Tunde Adesemi"></div>
    <div class="slot__info"><div class="slot__time">11:30 AM</div><div class="slot__name">Tunde Adesemi</div><div class="slot__topic">Real Estate Investing</div></div>
  </div>
  <div class="slot" style="top:948px">
    <div class="slot__photo" role="img" aria-label="Portrait of main speaker Marcus Oyelowo"></div>
    <div class="slot__info"><div class="slot__time">12:15 PM</div><div class="slot__name">Marcus Oyelowo</div><div class="slot__topic">(Main Speaker)<br>Training Topic TBA</div></div>
  </div>

  <h1 class="headline headline--attention">
    <span class="headline__thin">Attention Real</span>
    <span class="headline__bold">Estate Agents</span>
  </h1>

  <div class="invite">Please join<strong>us for our</strong></div>

  <h2 class="headline headline--expo">
    <span class="line line--thin">Quarterly</span>
    <span class="line line--mixed line--thin">Real <b>Estate</b></span>
    <span class="line line--yellow">Training</span>
    <span class="line line--yellow">Expo</span>
  </h2>

  <div class="schedule">
    <div class="schedule__days">The 2nd Saturday of<br>February, May, August<br>and November</div>
    <div class="schedule__next">Our next training expo</div>
    <div class="schedule__time">is from 9 am to 1 pm</div>
  </div>

  <div class="venue">
    <svg class="venue__pin" viewBox="0 0 40 56" aria-hidden="true">
      <path d="M20 2C10 2 3 9.5 3 19c0 13 17 34 17 34s17-21 17-34C37 9.5 30 2 20 2z" fill="var(--white)"/>
      <circle cx="20" cy="19" r="7" fill="var(--teal-light)"/>
    </svg>
    <p class="venue__text">At Marlowe Suites Fernridge Station 4187 Copperleaf Lane, Greenbelt, MD 20770.</p>
  </div>

  <footer class="contact">
    <p class="contact__lead">For more information<br>call Desmond Pryce at</p>
    <p class="contact__phone">
      <svg viewBox="0 0 34 34" aria-hidden="true">
        <circle cx="17" cy="17" r="16" fill="var(--white)"/>
        <path d="M11 9c1-1 2-1 3 0l2 3c.6 1 .4 1.8-.4 2.5l-1 1c.8 2 2.4 3.6 4.4 4.4l1-1c.7-.8 1.5-1 2.5-.4l3 2c1 1 1 2 0 3l-1.5 1.5C21 27 7 13 9.5 10.5z" fill="var(--teal-main)"/>
      </svg>(240) 555-0192</p>
    <p class="contact__email">Or email<br>dpryce@harborsummithomes.example</p>
  </footer>
</main>
</body>
</html>
```